The Harvest Compass

Cutting Through the Noise to What Actually Works.

Nutrition book

Target Market(s)

People looking to be or get healthy and eat right.

```html
<!DOCTYPE html>
<html lang="en">
<head>
<meta charset="utf-8">
<title>The Harvest Compass — Book Cover</title>
<link rel="stylesheet" href="https://fonts.googleapis.com/css2?family=DM+Serif+Display&family=Open+Sans:wght@400;500;600&display=swap">
<style>
  :root {
    --backdrop: #e8e3da;
    --cover: #f5f1e3;
    --ink: #141414;
    --leaf: #4f8a2b;
    --badge: #3f7a2f;
    --badge-text: #f3f1e6;
    --paper-light: #f2f2ef;
    --paper-shade: #c9c8c2;
  }
  * { margin: 0; padding: 0; box-sizing: border-box; }
  html, body {
    width: 1200px;
    height: 1200px;
    overflow: hidden;
    background: var(--backdrop);
  }
  .book-cover {
    position: absolute;
    left: 220px;
    top: 30px;
    width: 760px;
    height: 1140px;
    background: var(--cover);
    box-shadow: 0 6px 24px rgba(0,0,0,0.12);
    overflow: hidden;
  }
  .paper-ball {
    position: absolute;
    left: 275px;
    top: 30px;
    width: 190px;
    height: 160px;
    border-radius: 46% 54% 50% 48% / 52% 46% 54% 48%;
    background: radial-gradient(circle at 40% 35%, var(--paper-light), var(--paper-shade));
  }
  .title {
    position: absolute;
    left: 0;
    top: 185px;
    width: 100%;
    font-family: "DM Serif Display", Georgia, serif;
    font-weight: 400;
    color: var(--ink);
    line-height: 0.86;
  }
  .title-line { display: block; white-space: nowrap; }
  .title-the {
    font-size: 150px;
    padding-left: 230px;
    letter-spacing: -2px;
  }
  .title-main {
    font-size: 150px;
    padding-left: 140px;
    letter-spacing: -2px;
  }
  .title-accent {
    font-size: 128px;
    padding-left: 215px;
    color: var(--leaf);
    letter-spacing: -1px;
  }
  .title-underline {
    position: absolute;
    left: 440px;
    top: 570px;
  }
  .food-fork {
    position: absolute;
    left: 285px;
    top: 600px;
    width: 130px;
    height: 390px;
    border-radius: 60px 60px 14px 14px;
    background: linear-gradient(180deg,
      #7ea84a 0%, #c8d79a 18%, #e9a071 32%, #e06a3a 44%,
      #8a3c5c 56%, #d8402e 66%, #2f6a28 78%, #a56a3a 90%, #8c5630 100%);
  }
  .tagline {
    position: absolute;
    left: 485px;
    top: 640px;
    width: 205px;
    font-family: "Open Sans", Arial, sans-serif;
    font-size: 25px;
    line-height: 1.25;
    color: var(--ink);
  }
  .promise-badge {
    position: absolute;
    left: 62px;
    top: 700px;
    width: 196px;
    height: 196px;
    border-radius: 50%;
    background: var(--badge);
    display: flex;
    align-items: center;
    justify-content: center;
    text-align: center;
    font-family: "Open Sans", Arial, sans-serif;
    font-size: 17px;
    font-weight: 500;
    letter-spacing: 0.16em;
    line-height: 1.5;
    color: var(--badge-text);
    text-transform: uppercase;
  }
  .author {
    position: absolute;
    left: 0;
    top: 1035px;
    width: 100%;
    text-align: center;
    font-family: "Open Sans", Arial, sans-serif;
    font-size: 22px;
    font-weight: 600;
    letter-spacing: 0.32em;
    color: var(--ink);
  }
</style>
</head>
<body>
  <main class="book-cover">
    <div class="paper-ball" role="img" aria-label="Photo of a crumpled ball of white paper"></div>

    <h1 class="title">
      <span class="title-line title-the">The</span>
      <span class="title-line title-main">harvest</span>
      <span class="title-line title-accent">Compass</span>
    </h1>

    <svg class="title-underline" width="240" height="24" viewBox="0 0 240 24" aria-hidden="true">
      <path d="M4 14 C 70 8, 150 8, 226 12 L 232 6" fill="none" stroke="var(--leaf)" stroke-width="5" stroke-linecap="round"/>
    </svg>

    <div class="food-fork" role="img" aria-label="Photo of a wooden fork stacked with lettuce, avocado, salmon, red onion, tomato and spinach"></div>

    <p class="tagline">Cutting through the noise to what actually works.</p>

    <div class="promise-badge"><p>Real<br>answers<br>for a<br>healthier<br>tomorrow</p></div>

    <p class="author">YOUR NAME HERE</p>
  </main>
</body>
</html>
```